Velvet Dawn - 5 different skin care lotion bottles label designs

Packaging size labels see download files.
Every bottle has a front and a back label. They will be glued on the bottles.
Brand name is Velvet Dawn. See uploaded logo. It's our private label.
We would like to have a uniform as possible appearance of the products (CI).
Please use background graphics.
Only Adobe Illustrator files.

Here are the download files (sizes, etc and more details):
www.plumhaven.de/2014/BriefHub/5labels.zip
Updates

To all, I've uploaded PDF files for 4 bottles. One bottle is already Illustrator, like we want to get the label design. Helga

Reason: We think the time window was to short.

```html
<!DOCTYPE html>
<html lang="en">
<head>
<meta charset="utf-8">
<title>Velvet Dawn Skin Care Lotion Label</title>
<link rel="stylesheet" href="https://fonts.googleapis.com/css2?family=Open+Sans:wght@400;600;700&display=swap">
<style>
  :root {
    --page-bg: #f2f2f2;
    --label-light: #cdeefa;
    --label-mid: #8fd3f0;
    --label-deep: #3fa6da;
    --ink-blue: #1d62a6;
    --band-blue: #1f5c9e;
    --white: #ffffff;
    --portrait-warm: #a8714a;
    --portrait-dark: #5a3a25;
  }
  * { box-sizing: border-box; margin: 0; padding: 0; }
  html, body {
    width: 1035px;
    height: 1200px;
    overflow: hidden;
    background: var(--page-bg);
  }
  .canvas {
    position: relative;
    width: 1035px;
    height: 1200px;
  }
  .label {
    position: absolute;
    left: 388px;
    top: 508px;
    width: 250px;
    height: 556px;
    border-radius: 10px;
    overflow: hidden;
    background: radial-gradient(ellipse at 50% 38%, var(--label-light) 0%, var(--label-mid) 45%, var(--label-deep) 100%);
    font-family: "Open Sans", Arial, sans-serif;
    color: var(--ink-blue);
    text-align: center;
  }
  .brand {
    position: absolute;
    top: 58px;
    left: 0;
    width: 100%;
    display: flex;
    align-items: center;
    justify-content: center;
    gap: 8px;
  }
  .brand-dot {
    width: 14px;
    height: 14px;
    border-radius: 50%;
    background: var(--ink-blue);
  }
  .brand-name {
    font-size: 20px;
    font-weight: 600;
    letter-spacing: 0.5px;
    color: var(--ink-blue);
  }
  .product-type {
    position: absolute;
    top: 143px;
    width: 100%;
    font-size: 18.5px;
    font-weight: 400;
    letter-spacing: 0.2px;
  }
  .product-scent {
    position: absolute;
    top: 166px;
    width: 100%;
    font-size: 22px;
    font-weight: 700;
  }
  .product-benefit {
    position: absolute;
    top: 199px;
    width: 100%;
    font-size: 13.5px;
    font-weight: 400;
    letter-spacing: 0.5px;
  }
  .usage-note {
    position: absolute;
    top: 219px;
    width: 100%;
    font-size: 9px;
    font-weight: 600;
  }
  .portrait {
    position: absolute;
    left: 34px;
    top: 240px;
    width: 186px;
    height: 286px;
    border-radius: 90px 90px 0 0;
    background: radial-gradient(ellipse at 50% 40%, var(--portrait-warm) 0%, var(--portrait-dark) 100%);
  }
  .volume-band {
    position: absolute;
    left: 0;
    bottom: 0;
    width: 100%;
    height: 32px;
    background: var(--band-blue);
    color: var(--white);
    font-size: 14px;
    font-weight: 700;
    line-height: 32px;
  }
</style>
</head>
<body>
  <main class="canvas">
    <section class="label">
      <div class="brand">
        <span class="brand-dot"></span>
        <span class="brand-name">VELVET DAWN</span>
      </div>
      <p class="product-type">SKIN CARE LOTION</p>
      <p class="product-scent">HONEY ALMOND</p>
      <p class="product-benefit">Moisturizes and Smooths</p>
      <p class="usage-note">For external use only.</p>
      <div class="portrait" role="img" aria-label="Portrait photograph of a model with shoulder-length brown hair"></div>
      <div class="volume-band">591 ml /20 fl Oz</div>
    </section>
  </main>
</body>
</html>
```